Redesign Website for Tandara Flame

I have an existing website on https://www.tandaraflame-example.com.au/ and would like to have this redesigned professionally with new content (please refer to word document). We are fire protection engineers providing fire services design expertise and engineering design to a range of different clients.

We also provide drafting services to clients in the form of completing final commissioning documentation such as 'as-installed' drawings and fire services block plans to ensure compliance with the building code and relevant Australian Standards.

Target Market(s)

Builders, Architects, Consultants, Project Managers

Industry/Entity Type

Engineering Consultant

Coding

Coded - Design and coding required

Number of Pages Required

4 page

Font styles to use
Sans Serif

Requirements
Must have
• Home and about Page, fire services design page, fire block plans page, contact us page (4 Pages).

The website colour choice must match or compliment the new company logo.
Nice to have
• Quality photos of fire services installations in buildings to Australian Standards.

A website similar to this would be ideal http://corbellpyro-example.com.au
Should not have
• Stolen licensed photos

```html
<!DOCTYPE html>
<html lang="en">
<head>
<meta charset="utf-8">
<title>Tandara Flame – Fire Protection Engineers</title>
<link href="https://fonts.googleapis.com/css2?family=Oswald:wght@500&family=Poppins:wght@400;500;600&display=swap" rel="stylesheet">
<style>
:root{
  --orange:#f4952a;
  --orange-dark:#e9861a;
  --ink:#444;
  --grey:#6e6e6e;
  --grey-soft:#8a8a8a;
  --pale:#f3f3f3;
  --dark:#3e3e3e;
  --white:#fff;
}
*{margin:0;padding:0;box-sizing:border-box}
html,body{width:1200px;height:3517px;overflow:hidden;background:var(--white)}
body{position:relative;font-family:'Poppins',sans-serif;color:var(--ink)}
.abs{position:absolute}
.section-title{position:absolute;left:0;width:1200px;text-align:center;font-family:'Poppins',sans-serif;font-weight:500;font-size:33px;letter-spacing:1px;color:var(--grey)}
.section-title span{color:var(--orange)}
.section-title::after{content:"";display:block;width:36px;height:2px;background:#888;margin:14px auto 0}
.btn-outline{position:absolute;display:flex;align-items:center;justify-content:center;border:2px solid var(--orange);color:var(--ink);font-size:14px;font-weight:500;letter-spacing:.5px;text-decoration:none;background:transparent}
.btn-outline.dark{border-color:var(--ink)}
/* header */
.brand{left:160px;top:72px;font-size:23px;font-weight:500;color:var(--orange);letter-spacing:.5px}
.hero-photo{left:0;top:0;width:1200px;height:600px;clip-path:polygon(498px 0,1200px 0,1200px 539px,730px 410px,545px 330px);background:linear-gradient(135deg,#5b5e62 0%,#8b8e91 35%,#b4b6b7 55%,#6a6c6e 80%,#3d3f41 100%)}
.nav{left:543px;top:50px;display:flex;gap:22px;font-size:13.5px;color:var(--white);letter-spacing:.2px}
.nav a{color:var(--white);text-decoration:none}
.nav a.active{color:var(--orange)}
.hero-title{left:160px;top:200px;font-family:'Oswald',sans-serif;font-weight:500;font-size:39px;line-height:42px;color:var(--orange);letter-spacing:.5px}
.hero-sub{left:161px;top:290px;font-size:16.5px;line-height:23px;color:var(--grey-soft);letter-spacing:.8px;font-weight:500}
.btn-solid{left:160px;top:382px;width:138px;height:41px;background:var(--orange);color:var(--white);font-size:13.5px;font-weight:500;display:flex;align-items:center;justify-content:center;text-decoration:none}
/* about */
.about{left:0;top:687px;width:1200px;height:490px;background:linear-gradient(180deg,#f6f6f6,#ececec 60%,#f2f2f2)}
.about .section-title{top:14px}
.about-copy{position:absolute;left:164px;top:88px;width:872px;text-align:center;font-size:14px;line-height:23px;color:var(--grey)}
.about-copy p{margin-bottom:13px}
.about-copy strong{color:var(--orange);font-weight:600}
/* services */
.services{left:0;top:1177px;width:1200px;height:578px}
.services .section-title{top:86px}
.diagram{position:absolute;left:0;top:0}
.svc{position:absolute;font-size:14px;line-height:20px;color:var(--ink)}
.svc.right{text-align:right}
.svc.lead{color:var(--orange);font-weight:500;width:200px;text-align:center}
.wordmark{position:absolute;left:0;width:1200px;top:500px;text-align:center;font-size:40px;font-weight:500;color:var(--orange);letter-spacing:1px}
/* portfolio */
.portfolio{left:0;top:1755px;width:1200px;height:740px;background:var(--pale);clip-path:polygon(0 0,1200px 0,1200px 620px,600px 740px,0 620px)}
.portfolio .section-title{top:94px}
.tile{position:absolute}
.tile.overlay{background:var(--orange);color:var(--white);text-align:center;padding-top:48px}
.tile.overlay h3{font-weight:500;font-size:16px;margin-bottom:12px}
.tile.overlay p{font-size:12.5px;line-height:20px;padding:0 24px}
.tile.overlay .go{width:30px;height:30px;border:1.5px solid var(--white);border-radius:50%;margin:16px auto 0;display:flex;align-items:center;justify-content:center}
/* why */
.why .section-title{top:2590px}
.why-text{position:absolute;top:2788px;width:270px;text-align:center;font-size:14px;line-height:22px;color:var(--grey)}
/* footer */
.footer{left:0;top:3026px;width:1200px;height:491px;background:var(--dark);clip-path:polygon(0 131px,600px 0,1200px 131px,1200px 491px,0 491px)}
.footer-brand{left:0;width:1200px;top:3170px;text-align:center;font-size:31px;font-weight:500;color:var(--orange);letter-spacing:1px}
.contact{position:absolute;top:3335px;width:300px;text-align:center;color:var(--white)}
.contact h4{font-size:15px;font-weight:600;letter-spacing:.5px;margin-bottom:6px}
.contact p{font-size:14.5px;line-height:24px;color:#e6e6e6}
.footer-rule{left:0;top:3463px;width:1200px;height:1px;background:#585858}
.legal{top:3482px;font-size:13.5px;color:#e6e6e6}
</style>
</head>
<body>

<!-- Header & hero -->
<div class="abs hero-photo" role="img" aria-label="Photo of a building plant room ceiling with fire services pipework"></div>
<svg class="abs" style="left:0;top:0" width="1200" height="620" viewBox="0 0 1200 620">
  <polyline points="730,410 1154,598 1200,580" fill="none" stroke="var(--orange)" stroke-width="2"/>
  <polygon points="729,434 680,518 584,518 535,434 584,350 680,350" fill="var(--white)" stroke="var(--orange)" stroke-width="3"/>
  <defs><linearGradient id="pump" x1="0" y1="0" x2="1" y2="1"><stop offset="0" stop-color="#8e9296"/><stop offset=".5" stop-color="#b2363a"/><stop offset="1" stop-color="#6b6e70"/></linearGradient></defs>
  <polygon points="719,434 675,510 589,510 545,434 589,358 675,358" fill="url(#pump)" role="img" aria-label="Photo of red fire pump sets"/>
  <polygon points="590,30 584,22 572,22 566,30 572,38 584,38" fill="none" stroke="var(--orange)" stroke-width="1.5"/>
</svg>
<div class="abs brand">Tandara Flame</div>
<nav class="abs nav">
  <a class="active" href="#">ABOUT US</a>
  <a href="#">FIRE SERVICES DESIGN</a>
  <a href="#">FIRE BLOCK PLANS</a>
  <a href="#">CONTACT US</a>
</nav>
<h1 class="abs hero-title">WE ARE FIRE<br>PROTECTION ENGINEERS</h1>
<p class="abs hero-sub">PROVIDING FIRE SERVICES DESIGN<br>EXPERTISE AND ENGINEERING DESIGN<br>TO A RANGE OF DIFFERENT CLIENTS.</p>
<a class="abs btn-solid" href="#">CALL US TODAY</a>
<svg class="abs" style="left:90px;top:627px" width="62" height="56" viewBox="0 0 62 56"><polygon points="59,28 45,53 17,53 3,28 17,3 45,3" fill="none" stroke="var(--orange)" stroke-width="3"/></svg>

<!-- About -->
<section class="abs about" role="img" aria-label="Faint background photo of a building interior">
  <h2 class="section-title">ABOUT <span>TANDARA FLAME</span></h2>
  <div class="about-copy">
    <p><strong>Tandara Flame</strong> is a company based in Sydney providing the Australian market expertise in the field of fire safety.</p>
    <p>Our mission is to assist builders, architects, fire contractors, consultants and project managers with the preparation of fire services design and specifications to meet regulatory requirements for Complying Development Certificate (CDC), Development Applications (DA) or Council Fire Orders.</p>
    <p>We also provide fire services design peer review and sign-off under the new Fire Services Design (FSD) class of the Fire Protection Accreditation Scheme (FPAS) and the preparation of a Clause 164B objection letter to exempt certain building work on fire safety systems be exempt from compliance with the BCA and relevant standards.</p>
    <p>We strive to exceed our clients expectations in being competitively priced, meeting the project time constraints without the compromise in quality.</p>
  </div>
  <a class="btn-outline" style="left:501px;top:359px;width:200px;height:38px" href="#">CONTACT US TODAY</a>
</section>

<!-- Fire services design -->
<section class="abs services">
  <h2 class="section-title">FIRE <span>SERVICES DESIGN</span></h2>
  <svg class="diagram" width="1200" height="578" viewBox="0 1177 1200 578">
    <path d="M377,1755 A225,225 0 1 1 823,1755" fill="none" stroke="var(--orange)" stroke-width="2"/>
    <g stroke="#999" stroke-width="1.5" stroke-dasharray="2 3" fill="none">
      <line x1="491" y1="1474" x2="531" y2="1508"/>
      <line x1="714" y1="1474" x2="683" y2="1512"/>
      <line x1="446" y1="1500" x2="459" y2="1545"/>
      <line x1="774" y1="1510" x2="752" y2="1556"/>
      <line x1="379" y1="1585" x2="405" y2="1611"/>
      <line x1="830" y1="1590" x2="799" y2="1615"/>
      <line x1="345" y1="1675" x2="378" y2="1689"/>
      <line x1="859" y1="1675" x2="822" y2="1694"/>
    </g>
    <line x1="599" y1="1453" x2="598" y2="1499" stroke="var(--orange)" stroke-width="1.5"/>
    <g fill="var(--orange)">
      <circle cx="531" cy="1508" r="4.5"/><circle cx="598" cy="1499" r="4.5"/><circle cx="683" cy="1512" r="4.5"/>
      <circle cx="459" cy="1545" r="4.5"/><circle cx="752" cy="1556" r="4.5"/><circle cx="405" cy="1611" r="4.5"/>
      <circle cx="799" cy="1615" r="4.5"/><circle cx="378" cy="1689" r="4.5"/><circle cx="822" cy="1694" r="4.5"/>
    </g>
    <!-- hexagon nodes -->
    <g fill="var(--white)" stroke="var(--orange)" stroke-width="1.5">
      <polygon points="525,1440 508,1469 474,1469 457,1440 474,1411 508,1411"/>
      <polygon points="748,1440 731,1469 697,1469 680,1440 697,1411 731,1411"/>
      <polygon points="446,1492 429,1521 395,1521 378,1492 395,1463 429,1463"/>
      <polygon points="842,1492 825,1521 791,1521 774,1492 791,1463 825,1463"/>
      <polygon points="379,1573 362,1602 328,1602 311,1573 328,1544 362,1544"/>
      <polygon points="898,1573 881,1602 847,1602 830,1573 847,1544 881,1544"/>
      <polygon points="345,1667 328,1696 294,1696 277,1667 294,1638 328,1638"/>
      <polygon points="927,1667 910,1696 876,1696 859,1667 876,1638 910,1638"/>
    </g>
    <polygon points="633,1420 616,1449 582,1449 565,1420 582,1391 616,1391" fill="var(--orange)"/>
    <!-- icons -->
    <g fill="none" stroke="#555" stroke-width="1.4">
      <circle cx="599" cy="1420" r="13" stroke="var(--white)"/><circle cx="599" cy="1420" r="6" stroke="var(--white)"/>
      <rect x="483" y="1426" width="16" height="28" rx="2"/><circle cx="491" cy="1444" r="4"/><line x1="487" y1="1432" x2="495" y2="1432"/>
      <rect x="702" y="1430" width="24" height="8"/><path d="M706,1438 v6 h16 v-6"/><path d="M708,1448 l-1,5 M714,1448 v5 M720,1448 l1,5"/>
      <path d="M400,1487 h6 l8,-7 v24 l-8,-7 h-6 z"/><path d="M419,1485 q5,7 0,14 M424,1481 q8,11 0,22"/>
      <rect x="800" y="1484" width="16" height="20" rx="2"/><path d="M803,1484 q5,-10 10,0"/><circle cx="808" cy="1494" r="4"/>
      <rect x="340" y="1568" width="10" height="20" rx="3"/><path d="M345,1568 v-6 l10,-5 M342,1560 h8"/>
      <path d="M856,1583 h16 M858,1583 v-6 q6,-12 12,0 v6"/><path d="M864,1559 v-5 M852,1565 l-4,-3 M876,1565 l4,-3"/>
      <rect x="297" y="1653" width="28" height="8"/><path d="M301,1661 h20 v12 h-20 z"/><circle cx="311" cy="1676" r="4"/>
      <rect x="877" y="1656" width="32" height="22" rx="2"/><path d="M882,1661 h22"/><path d="M886,1672 l8,-6 M890,1672 h-4 v-4"/>
    </g>
  </svg>
  <div class="svc lead" style="left:499px;top:177px">Fire Hose Reels</div>
  <div class="svc right" style="right:750px;top:225px">EWIS / SSISEP</div>
  <div class="svc" style="left:762px;top:216px">Automatic Smoke Detection<br>&amp; Alarm Systems</div>
  <div class="svc right" style="right:839px;top:282px">Occupant Warning<br>Systems</div>
  <div class="svc" style="left:857px;top:304px">Fire Hydrants</div>
  <div class="svc right" style="right:906px;top:371px">Portable Fire<br>Extinguishers</div>
  <div class="svc" style="left:913px;top:373px">Emergency<br>Lighting</div>
  <div class="svc right" style="right:938px;top:480px">Smoke Alarms</div>
  <div class="svc" style="left:942px;top:480px">Exit Signs</div>
  <div class="wordmark">TANDARA FLAME</div>
</section>

<!-- Portfolio -->
<section class="abs portfolio">
  <h2 class="section-title">OUR <span>PORTFOLIO</span></h2>
</section>
<div class="tile" style="left:161px;top:1930px;width:209px;height:172px;background:linear-gradient(135deg,#8b8b86,#c4c1bb 50%,#b33b3b 75%,#9a9894)" role="img" aria-label="Photo of hydrant booster valves on a block wall"></div>
<div class="tile" style="left:161px;top:2116px;width:209px;height:209px;background:linear-gradient(135deg,#7a4a3e,#a0614e 40%,#3f5e8f 65%,#b83a3a)" role="img" aria-label="Photo of fire valve assembly on a brick wall"></div>
<div class="tile overlay" style="left:385px;top:1930px;width:209px;height:229px">
  <h3>LOREM IPSUM</h3>
  <p>Lorem Ipsum is simply dummy text of the printing and typesetting</p>
  <div class="go"><svg width="14" height="12" viewBox="0 0 14 12"><path d="M1,6 h11 M8,2 l4,4 -4,4" fill="none" stroke="#fff" stroke-width="1.5"/></svg></div>
</div>
<div class="tile" style="left:385px;top:2174px;width:209px;height:151px;background:linear-gradient(160deg,#d8d8d6,#9e9e9b 50%,#c6b36a 85%)" role="img" aria-label="Photo of an underground car park corridor"></div>
<div class="tile" style="left:607px;top:1930px;width:209px;height:152px;background:linear-gradient(160deg,#4f5356,#7c8085 50%,#2c2e30)" role="img" aria-label="Photo of a car park entry with glass balustrade"></div>
<div class="tile" style="left:607px;top:2095px;width:209px;height:230px;background:linear-gradient(170deg,#9a9c9e,#c9c9c7 55%,#7d7f80)" role="img" aria-label="Photo of workers inspecting a basement car park"></div>
<div class="tile" style="left:830px;top:1930px;width:209px;height:210px;background:linear-gradient(160deg,#e9e8e6,#cfcdca 60%,#8d8a86)" role="img" aria-label="Photo of a corridor with a fire extinguisher"></div>
<div class="tile" style="left:830px;top:2154px;width:209px;height:171px;background:linear-gradient(135deg,#e3e3e3,#c83a3a 45%,#d9d9d9 75%,#a9a9a9)" role="img" aria-label="Photo of a red fire hose reel"></div>
<a class="btn-outline" style="left:539px;top:2366px;width:122px;height:38px" href="#">LOAD MORE</a>

<!-- Why choose us -->
<section class="why">
  <h2 class="section-title">WHY <span>CHOOSE US</span></h2>
  <svg class="abs" style="left:0;top:2660px" width="1200" height="120" viewBox="0 2660 1200 120">
    <g fill="none" stroke="var(--orange)" stroke-width="1.5">
      <polygon points="350,2719 323,2765 269,2765 242,2719 269,2673 323,2673"/>
      <polygon points="653,2719 626,2765 572,2765 545,2719 572,2673 626,2673"/>
      <polygon points="956,2719 929,2765 875,2765 848,2719 875,2673 929,2673"/>
    </g>
    <g fill="none" stroke="#555" stroke-width="1.6">
      <circle cx="296" cy="2719" r="21"/><circle cx="296" cy="2719" r="15"/><path d="M288,2719 l6,6 10,-11"/>
      <circle cx="599" cy="2719" r="21"/><circle cx="599" cy="2719" r="15"/><path d="M591,2722 h4 v9 h-4 z M595,2722 l5,-10 q3,0 2,5 h6 q2,1 1,3 l-2,10 h-12"/>
      <circle cx="902" cy="2719" r="21"/><circle cx="902" cy="2719" r="15"/><path d="M907,2712 q-5,-4 -9,0 q-2,4 4,6 q6,2 4,6 q-4,4 -10,0 M902,2707 v24"/>
    </g>
  </svg>
  <p class="why-text" style="left:161px">We pride ourselves on our prompt service and delivery of all of our projects. You can rely on us to meet your project deadlines!</p>
  <p class="why-text" style="left:464px">Our customer service and our output is guaranteed to be of the highest quality. You will not be disappointed.</p>
  <p class="why-text" style="left:767px">We strive to always be competitively priced are very competitively priced.</p>
  <a class="btn-outline dark" style="left:500px;top:2896px;width:200px;height:38px" href="#">CONTACT US TODAY</a>
</section>

<!-- Footer -->
<footer>
  <div class="abs footer"></div>
  <div class="abs footer-brand">TANDARA FLAME</div>
  <svg class="abs" style="left:0;top:3250px" width="1200" height="70" viewBox="0 3250 1200 70">
    <g fill="#4f4f4f">
      <polygon points="328,3283 313,3309 283,3309 268,3283 283,3257 313,3257"/>
      <polygon points="629,3283 614,3309 584,3309 569,3283 584,3257 614,3257"/>
      <polygon points="940,3283 925,3309 895,3309 880,3283 895,3257 925,3257"/>
    </g>
    <g fill="var(--orange)">
      <path d="M291,3276 q2,-3 5,0 l1,3 q0,2 -2,3 q2,4 6,6 q1,-2 3,-2 l3,1 q3,3 0,5 q-4,3 -10,-2 q-6,-5 -6,-10 z"/>
      <path d="M599,3294 q-9,-10 -9,-16 a9,9 0 0 1 18,0 q0,6 -9,16 z M599,3274 a4,4 0 1 0 0.1,0 z" fill-rule="evenodd"/>
      <path d="M901,3277 h18 v2 l-9,6 -9,-6 z M901,3281 l9,6 9,-6 v9 h-18 z"/>
    </g>
  </svg>
  <div class="contact" style="left:148px"><h4>PHONE</h4><p>+614 00 555 019</p></div>
  <div class="contact" style="left:449px"><h4>ADDRESS</h4><p>123 Building Name, Street Name,<br>City Name, State XY-123456</p></div>
  <div class="contact" style="left:760px"><h4>EMAIL</h4><p>info@tandaraflame-example.com.au</p></div>
  <div class="abs footer-rule"></div>
  <div class="abs legal" style="left:162px">Copyright © 2021 Tandara Flame. All Rights Reserved.</div>
  <div class="abs legal" style="right:165px">ABN: 00 000 555 019</div>
</footer>

</body>
</html>
```